Willowmere Network for Sensory Play and Family Wellbeing

We need a simple design to show what the non-profit association, its board of directors, and trainings do. Having the opportunity to upload videos and photos of the activities we do with the children. The page is focused on teachers, psychologists, special educators, therapists, mothers and parents. We want a simple and easy to use page where you can find references of kinders who are endorsed by the association, professionals endorsed by the association and have links to articles and pages that are linked to our association.

Target Market(s)

Teachers, psychologists, mothers, therapists,

Coding

Coded - Design and coding required

Number of Pages Required

3 page

Font styles to use
Sans Serif

Colors
34a6d7
e667a6
fbf289
33b8a4

Requirements
Must have
• Association logo, photos of children that can be modified, videos and informational capsules can be uploaded.
Nice to have
• that you can upload photos, logo colors that are light pink and light turquoise, general information of the association, informative blog, upload videos
Should not have
• Black colors

```html
<!DOCTYPE html>
<html lang="en">
<head>
<meta charset="utf-8">
<title>Willowmere Network for Sensory Play and Family Wellbeing</title>
<link href="https://fonts.googleapis.com/css2?family=Poppins:wght@600;700&family=Roboto:wght@400;500;700&display=swap" rel="stylesheet">
<style>
:root{
  --blue:#34a6d7; --blue-deep:#2a8fc4; --pink:#e667a6; --yellow:#fbf289;
  --teal:#33b8a4; --teal-dark:#1f9e8b; --text:#555b66; --heading:#2ea597;
  --light:#f2f2f2; --white:#fff;
}
*{box-sizing:border-box;margin:0;padding:0}
html,body{width:1200px;height:3840px;overflow:hidden}
body{position:relative;font-family:"Roboto",sans-serif;color:var(--text);background:var(--white)}
.abs{position:absolute}
.btn{position:absolute;display:flex;align-items:center;justify-content:center;gap:8px;border-radius:26px;color:#fff;font:700 15px "Roboto",sans-serif;text-transform:uppercase;letter-spacing:.3px}
.btn .arr{width:15px;height:15px;border-radius:50%;background:#fff;display:inline-flex;align-items:center;justify-content:center}
.btn .arr::after{content:"";border-left:6px solid var(--teal);border-top:4px solid transparent;border-bottom:4px solid transparent;margin-left:2px}
.btn.blue .arr::after{border-left-color:var(--blue)}
.teal{background:var(--teal)} .blue{background:var(--blue)}
h2.section-title{position:absolute;left:0;width:1200px;text-align:center;font:700 35px "Poppins",sans-serif;color:var(--heading);text-transform:uppercase;letter-spacing:-.5px}
/* hero */
.hero-photo{left:0;top:0;width:1200px;height:840px;background:linear-gradient(160deg,#6b7483 0%,#4e5b72 30%,#3a5fa8 60%,#2c3f8a 80%,#1b5a3e 100%)}
.hero-shade{left:0;top:0;width:1200px;height:180px;background:linear-gradient(#0000007a,#0000)}
.topline{left:0;top:0;width:1200px;height:4px;background:var(--blue)}
.brand{left:110px;top:60px;display:flex;align-items:center;gap:10px;color:#fff;font:700 20px "Roboto",sans-serif}
.brand i{width:38px;height:38px;border-radius:50%;background:var(--teal);display:block}
.call{left:690px;top:24px;display:flex;align-items:center;gap:10px;color:#fff}
.call .ring{width:42px;height:42px;border:2px solid #fff;border-radius:50%;display:flex;align-items:center;justify-content:center}
.call small{display:block;font-size:14px}
.call b{font-size:21px;font-weight:700}
.nav{left:352px;top:100px;display:flex;gap:23px;color:#fff;font:500 15px "Roboto",sans-serif;align-items:center}
.nav .on{color:var(--teal)}
.hero-title{left:253px;top:265px;width:694px;background:var(--blue);color:#fff;text-align:center;font:700 25px/38px "Poppins",sans-serif;padding:15px 16px;text-transform:uppercase;white-space:nowrap}
.slide-arrow{top:350px;width:42px;height:42px;border:2px solid #fff;border-radius:50%}
/* welcome */
.welcome-art{left:110px;top:810px;width:450px;height:415px;border-radius:40px;background:linear-gradient(135deg,#4fc0b1 0%,#3aa597 55%,#e78a86 100%)}
.welcome-title{left:600px;top:852px;font:700 30px "Poppins",sans-serif;color:var(--heading);text-transform:uppercase}
.welcome-text{left:600px;top:912px;width:490px;font-size:15px;line-height:28.5px;color:#777}
/* tiles */
.tile{top:1328px;width:240px;height:280px;display:flex;flex-direction:column;align-items:center;justify-content:center;color:#fff;text-align:center;padding:0 18px}
.tile h3{font:700 16px "Roboto",sans-serif;text-transform:uppercase;margin-top:14px}
.tile p{font-size:14px;line-height:21px;margin-top:10px}
.tile svg{width:54px;height:60px}
.tile.yellow{color:#333}
/* videos */
.video{top:1773px;width:310px;height:245px;background:linear-gradient(#5a6f97,#2e3f6e)}
.video .play{position:absolute;left:137px;top:97px;width:38px;height:38px;border-radius:50%;background:var(--blue);display:flex;align-items:center;justify-content:center}
.video .play::after{content:"";border-left:13px solid #fff;border-top:8px solid transparent;border-bottom:8px solid transparent;margin-left:4px}
.video h4{position:absolute;left:0;width:100%;top:182px;text-align:center;color:#fff;font:500 16px "Roboto",sans-serif}
.video .meta{position:absolute;left:0;width:100%;top:212px;text-align:center;color:#fff;font-size:14px}
.video .meta span{color:var(--teal)}
/* gallery */
.gallery-band{left:0;top:2208px;width:1200px;height:430px;background:var(--light)}
.shot{top:2311px;width:232px;height:277px}
/* articles */
.article{top:2811px;width:305px;height:305px;background:#fff;box-shadow:0 3px 10px #0002;border-bottom:3px solid var(--blue)}
.article .pic{height:200px}
.article h4{text-align:center;font:500 17px/25px "Roboto",sans-serif;color:#333;margin-top:10px;padding:0 16px}
.article .meta{text-align:center;font-size:13px;color:#666;margin-top:10px}
/* footer */
.foot-h{font:500 19px "Roboto",sans-serif;color:#fff;text-transform:uppercase}
.field{position:absolute;height:40px;background:#fff;border:1px solid #ddd;font-size:14px;color:#555;padding:11px 18px}
.links{left:641px;top:3493px;list-style:none;color:#fff;font-size:15px;line-height:30px}
.links li::before{content:"";display:inline-block;width:0;height:0;border-left:6px solid var(--pink);border-top:4px solid transparent;border-bottom:4px solid transparent;margin-right:14px}
.contact{left:808px;top:3493px;color:#fff;font-size:15px;line-height:24px}
.contact div{display:flex;gap:16px;margin-bottom:10px}
.contact i{width:12px;height:12px;border-radius:50%;background:var(--pink);margin-top:6px;flex:none}
.social{top:3670px;width:32px;height:32px;border-radius:50%}
</style>
</head>
<body>

<!-- Hero -->
<div class="abs hero-photo" role="img" aria-label="Photo of mothers and babies sitting on colourful mats during an early stimulation class"></div>
<div class="abs hero-shade"></div>
<div class="abs topline"></div>
<div class="abs brand"><i></i>Willowmere Network</div>
<div class="abs call">
  <div class="ring"><svg width="18" height="18" viewBox="0 0 24 24"><path fill="#fff" d="M6.6 10.8a15 15 0 006.6 6.6l2.2-2.2a1 1 0 011-.3 11.4 11.4 0 003.6.6 1 1 0 011 1V20a1 1 0 01-1 1A17 17 0 013 4a1 1 0 011-1h3.5a1 1 0 011 1c0 1.2.2 2.4.6 3.6a1 1 0 01-.3 1z"/></svg></div>
  <div><small>Call Us:</small><b>555-014-2290</b></div>
</div>
<div class="btn teal" style="left:921px;top:22px;width:165px;height:48px;">Donate Now <span class="arr"></span></div>
<nav class="abs nav">
  <span class="on">Home</span><span>About</span><span>Board of Directors</span><span>Training</span><span>Our Association</span><span>Articles</span><span>Contact</span>
  <svg width="16" height="16" viewBox="0 0 16 16"><circle cx="6.5" cy="6.5" r="5" fill="none" stroke="#fff" stroke-width="2"/><path d="M10 10l5 5" stroke="#fff" stroke-width="2"/></svg>
  <span>En ⌄</span>
</nav>
<div class="abs hero-title">Willowmere Network for Sensory Play<br>&amp; Family Wellbeing</div>
<div class="abs slide-arrow" style="left:33px"></div>
<div class="abs slide-arrow" style="left:1130px"></div>
<svg class="abs" style="left:0;top:630px" width="1200" height="220" viewBox="0 0 1200 220">
  <path d="M0 100 C220 20 420 10 700 60 C900 95 1060 80 1200 20 L1200 220 L0 220Z" fill="var(--teal)"/>
  <path d="M0 210 C160 80 380 60 660 100 C880 130 1060 110 1200 40 L1200 220 L0 220Z" fill="#fff"/>
</svg>

<!-- Welcome -->
<div class="abs welcome-art" role="img" aria-label="Framed photo of a class with families and their babies"></div>
<h2 class="abs welcome-title">Welcome to our Association</h2>
<p class="abs welcome-text">Lorem ipsum dolor sit amet, consectetur adipiscing elit, sed eiusmod tempor incididunt ut labore et dolore magna aliqua. Ut enim ad minim veniam, quis nostrud exercitation ullamco laboris nisi ut aliquip ex ea commodo consequat. Duis aute irure dolor in reprehenderit in voluptate velit esse cillum dolore eu fugiat nulla pariatur. Excepteur sint occaecat cupidatat non proident, sunt in culpa qui officia</p>
<div class="btn teal" style="left:599px;top:1123px;width:162px;height:51px;">Learn More <span class="arr"></span></div>

<!-- Audience tiles -->
<div class="abs tile" style="left:0;background:var(--blue)"><svg viewBox="0 0 54 60"><circle cx="27" cy="16" r="11" fill="none" stroke="#fff" stroke-width="3"/><path d="M6 58c0-14 9-22 21-22s21 8 21 22" fill="none" stroke="#fff" stroke-width="3"/></svg><h3>Teachers</h3></div>
<div class="abs tile" style="left:240px;background:var(--pink)"><svg viewBox="0 0 54 60"><circle cx="27" cy="16" r="11" fill="none" stroke="#fff" stroke-width="3"/><path d="M6 58c0-14 9-22 21-22s21 8 21 22" fill="none" stroke="#fff" stroke-width="3"/></svg><h3>Psychologists</h3></div>
<div class="abs tile yellow" style="left:480px;background:var(--yellow)"><svg viewBox="0 0 54 60"><rect x="3" y="8" width="48" height="38" fill="none" stroke="#333" stroke-width="3"/><path d="M12 20h30M12 28h22" stroke="#333" stroke-width="3"/></svg><h3>Special Educators</h3><p>Lorem ipsum dolor sit amet, consectetur adipiscing elit, sed do eiusmod tempor ut labore</p></div>
<div class="abs tile" style="left:720px;background:var(--teal)"><svg viewBox="0 0 54 60"><circle cx="27" cy="16" r="11" fill="none" stroke="#fff" stroke-width="3"/><path d="M6 58c0-14 9-22 21-22s21 8 21 22" fill="none" stroke="#fff" stroke-width="3"/></svg><h3>Therapists</h3></div>
<div class="abs tile" style="left:960px;background:var(--blue-deep)"><svg viewBox="0 0 54 60"><circle cx="17" cy="18" r="9" fill="none" stroke="#fff" stroke-width="3"/><circle cx="38" cy="18" r="9" fill="none" stroke="#fff" stroke-width="3"/><path d="M2 56c0-12 6-20 15-20s15 8 15 20M22 56c0-12 7-20 16-20s14 8 14 20" fill="none" stroke="#fff" stroke-width="3"/></svg><h3>Mothers &amp; Parents</h3></div>

<!-- Videos -->
<h2 class="section-title" style="top:1695px">Our Videos</h2>
<div class="abs video" style="left:111px" role="img" aria-label="Video still of a baby swimming class in a pool"><span class="play"></span><h4>Lorem ipsum dolor sit consectetur</h4><div class="meta"><span>◷</span> 20:00 &nbsp;&nbsp;|&nbsp;&nbsp; <span>◉</span> 5,681</div></div>
<div class="abs video" style="left:445px" role="img" aria-label="Video still of an instructor guiding mothers on floor mats"><span class="play"></span><h4>Lorem ipsum dolor sit consectetur</h4><div class="meta"><span>◷</span> 20:00 &nbsp;&nbsp;|&nbsp;&nbsp; <span>◉</span> 5,681</div></div>
<div class="abs video" style="left:778px" role="img" aria-label="Video still of parents dancing in a group session"><span class="play"></span><h4>Lorem ipsum dolor sit consectetur</h4><div class="meta"><span>◷</span> 20:00 &nbsp;&nbsp;|&nbsp;&nbsp; <span>◉</span> 5,681</div></div>
<div class="btn teal" style="left:508px;top:2063px;width:184px;height:46px;">Upload Videos <span class="arr"></span></div>

<!-- Gallery -->
<div class="abs gallery-band"></div>
<h2 class="section-title" style="top:2230px">Our Gallery</h2>
<div class="btn blue" style="left:905px;top:2243px;width:184px;height:43px;">Upload Photos <span class="arr"></span></div>
<div class="abs shot" style="left:111px;background:linear-gradient(#8c7a6c,#c9c2b8)" role="img" aria-label="Group photo of graduates holding certificates"></div>
<div class="abs shot" style="left:359px;background:linear-gradient(#9b9fa8,#3b4470)" role="img" aria-label="Participants seated at a table in a workshop"></div>
<div class="abs shot" style="left:608px;background:linear-gradient(#b7b3ae,#d8d6d2)" role="img" aria-label="Classroom with attendees taking notes"></div>
<div class="abs shot" style="left:856px;background:linear-gradient(#a9b3c8,#2c4fb0 60%,#2d8a44)" role="img" aria-label="Mothers and babies on colourful floor mats"></div>

<!-- Articles -->
<h2 class="section-title" style="top:2733px">Latest Articles</h2>
<div class="abs article" style="left:111px"><div class="pic" role="img" aria-label="Team of volunteers smiling together" style="background:linear-gradient(#9cc6c6,#5b6b6e)"></div><h4>Lorem ipsum dolor sit consectetur adipiscing elit, sed</h4><div class="meta">Posted by Mara Ellis &nbsp;|&nbsp; Apr 05, 2020</div></div>
<div class="abs article" style="left:447px"><div class="pic" role="img" aria-label="Families gathered in a therapy room" style="background:linear-gradient(#8f9aa8,#3c4250)"></div><h4>Lorem ipsum dolor sit consectetur adipiscing elit, sed</h4><div class="meta">Posted by Mara Ellis &nbsp;|&nbsp; Mar 25, 2020</div></div>
<div class="abs article" style="left:783px"><div class="pic" role="img" aria-label="Speaker presenting to an audience" style="background:linear-gradient(#8c7a6c,#c5bfb6)"></div><h4>Lorem ipsum dolor sit consectetur adipiscing elit, sed</h4><div class="meta">Posted by Mara Ellis &nbsp;|&nbsp; Mar 15, 2020</div></div>
<div class="btn teal" style="left:500px;top:3204px;width:200px;height:50px;">View All Artcles <span class="arr"></span></div>

<!-- Footer -->
<svg class="abs" style="left:0;top:3240px" width="1200" height="600" viewBox="0 0 1200 600">
  <path d="M0 120 C200 60 400 70 640 130 C880 180 1050 120 1200 0 L1200 600 L0 600Z" fill="var(--teal)"/>
  <path d="M0 140 C200 80 400 90 640 145 C880 195 1050 140 1200 40 L1200 600 L0 600Z" fill="#fff"/>
  <path d="M0 150 C200 95 400 100 640 160 C880 210 1050 160 1200 60 L1200 600 L0 600Z" fill="var(--blue)"/>
</svg>
<div class="abs foot-h" style="left:111px;top:3452px">Get in Touch</div>
<div class="field" style="left:111px;top:3493px;width:235px">First Name</div>
<div class="field" style="left:353px;top:3493px;width:235px">Last Name</div>
<div class="field" style="left:111px;top:3542px;width:235px">Email</div>
<div class="field" style="left:353px;top:3542px;width:235px">phone number</div>
<div class="field" style="left:111px;top:3591px;width:477px;height:75px">Message</div>
<div class="btn teal" style="left:111px;top:3683px;width:133px;height:46px;border-radius:24px">Submit</div>

<div class="abs foot-h" style="left:641px;top:3452px">Quick Links</div>
<ul class="abs links"><li>Home</li><li>About</li><li>Training</li><li>Articles</li><li>Contact Us</li></ul>

<div class="abs foot-h" style="left:808px;top:3452px">Contact Us</div>
<div class="abs contact">
  <div><i></i><span>14 Larkspur Lane, Brookhaven,<br>OR 97402</span></div>
  <div><i></i><span>(555) 014-2290</span></div>
  <div><i></i><span>(555) 017-3381</span></div>
  <div><i></i><span>hello@willowmerenetwork.org</span></div>
</div>
<div class="abs foot-h" style="left:641px;top:3675px">Stay Connected :</div>
<div class="abs social" style="left:842px;background:#3d5aa8"></div>
<div class="abs social" style="left:881px;background:var(--pink)"></div>

<div class="abs" style="left:111px;top:3778px;width:978px;height:1px;background:#ffffff66"></div>
<div class="abs" style="left:0;top:3798px;width:1200px;text-align:center;color:#fff;font-size:15px">© 2020 Willowmere Network &nbsp;| All Rights Reserved | Terms and Conditions</div>

</body>
</html>
```